Online-Marketing Material für Hundetraining
Zielgruppe
Hundetraining. Ich coache Hundehalter und unterstütze sie darin ihrem Hund Führung zu geben. Im Vordergrund steht die natürliche Kommunikation mit dem Hund - komplett ohne Leckerchen.
Aufgabenstellung
Ich brauche ein Design für eine Facebookwerbeanzeige. Der Titel meines Videokurses ist 'Gemeinsam stark im Alltag'. Inhaltlich geht es in dem Kurs darum, wie Hundehalter der akzeptierte Entscheidungsträger werden können, indem wir am Grundrespekt arbeiten und die eigene Führungskompetenzen ausbauen.

```html
<!DOCTYPE html>
<html lang="de">
<head>
<meta charset="utf-8">
<title>Rudelweg – Anzeige</title>
<link rel="stylesheet" href="https://fonts.googleapis.com/css2?family=Montserrat:wght@400;500;700&family=Open+Sans:wght@700&family=Yellowtail&display=swap">
<style>
  :root {
    --stage: #7b797a;
    --teal: #07b2aa;
    --white: #ffffff;
    --orange: #e08e1d;
    --photo-top: #8a6a58;
    --photo-mid: #b8977f;
    --photo-bottom: #ece8e4;
  }
  * { margin: 0; padding: 0; box-sizing: border-box; }
  html, body { width: 1200px; height: 864px; overflow: hidden; background: var(--stage); }
  .ad {
    position: absolute; left: 0; top: 71px;
    width: 1200px; height: 722px;
    background: var(--teal);
    overflow: hidden;
    font-family: "Montserrat", sans-serif;
  }
  .ad__photo {
    position: absolute; left: 0; top: 0; width: 580px; height: 722px;
    background: linear-gradient(180deg, var(--photo-top) 0%, var(--photo-mid) 60%, var(--photo-bottom) 100%);
  }
  .brand {
    position: absolute; left: 620px; top: 40px; width: 500px;
    display: flex; flex-direction: column; align-items: center; gap: 14px;
  }
  .brand__dot { width: 86px; height: 86px; border-radius: 50%; background: var(--white); }
  .brand__name {
    color: var(--white); font-weight: 700; font-size: 19px; letter-spacing: 0.5px;
  }
  .headline { font-size: 0; }
  .headline__line {
    position: absolute; height: 79px; background: var(--white); color: var(--teal);
    display: flex; align-items: center; justify-content: center;
    font-size: 53px; line-height: 1; white-space: nowrap;
  }
  .headline__line--one { left: 630px; top: 204px; width: 473px; font-weight: 700; }
  .headline__line--two { left: 611px; top: 297px; width: 514px; font-weight: 700; }
  .headline__line--three { left: 601px; top: 394px; width: 534px; font-weight: 500; }
  .tagline {
    position: absolute; left: 600px; top: 500px; width: 535px; text-align: center;
    font-family: "Yellowtail", cursive; color: var(--white); font-size: 50px; line-height: 1.2;
    white-space: nowrap;
  }
  .cta {
    position: absolute; left: 708px; top: 604px; width: 324px; height: 62px;
    border-radius: 24px; background: var(--orange); color: var(--white);
    display: flex; align-items: center; justify-content: center;
    font-family: "Open Sans", sans-serif; font-weight: 700; font-size: 28px;
    box-shadow: 0 6px 14px rgba(0,0,0,0.18);
  }
</style>
</head>
<body>
  <main class="ad">
    <div class="ad__photo" role="img" aria-label="Foto: Hund legt die Pfoten über die Schultern eines Mannes im weißen T-Shirt, von hinten gesehen"></div>

    <div class="brand">
      <span class="brand__dot"></span>
      <span class="brand__name">RUDELWEG.DE</span>
    </div>

    <h1 class="headline">
      <span class="headline__line headline__line--one">MEIN BESITZER</span>
      <span class="headline__line headline__line--two">TRAINIERT MICH</span>
      <span class="headline__line headline__line--three">OHNE LECKERLIS</span>
    </h1>

    <p class="tagline">und es funktioniert gut!</p>

    <span class="cta">INTERESSIERT?</span>
  </main>
</body>
</html>
```